New Business Card for General Contractor Marketing

Need a business card the is more like a marketing promotion of our services
Must be horizontal orientation, One Sided Only, Max font size, Organize the Services
#1 General Contractor for Realtors
Remodels – Renovations – Repairs
Water & Mold Damage Experts
Painting: Interior/ Exterior
Flooring: Wood / LVT / Carpet
Plumbing: Repairs & Upgrades
Electric: Lights & Energy Efficient Upgrades
Kitchen & Bath Remodels
Fast Inspections Repair Billed Thru Escrow
BrightHarborBuild.example
555-014-7390

Industry/Entity Type

General Contractor

Contact Information for Business Card

One Sided Only: #1 General Contractor for Realtors Remodels – Renovations – Repairs Water & Mold Damage Experts Painting: Interior/ Exterior Flooring: Wood / LVT / Carpet Plumbing: Repairs & Upgrades Electric: Lights & Energy Efficient Upgrades Kitchen & Bath Remodels Fast Inspections Repair Billed Thru Escrow BrightHarborBuild.example 555-014-7390

Colors
0054AA
0677BA
7BADD7
CADEEF
E8F1F8

Requirements
Must have
• One Sided Only: #1 General Contractor for Realtors Remodels – Renovations – Repairs Water & Mold Damage Experts Painting: Interior/ Exterior Flooring: Wood / LVT / Carpet Plumbing: Repairs & Upgrades Electric: Lights & Energy Efficient Upgrades Kitchen & Bath Remodels Fast Inspections Repair Billed Thru Escrow BrightHarborBuild.example 555-014-7390

```html
<!DOCTYPE html>
<html lang="en">
<head>
<meta charset="utf-8">
<title>Bright Harbor Build – Business Card</title>
<link href="https://fonts.googleapis.com/css2?family=Jost:wght@400;500;600&display=swap" rel="stylesheet">
<style>
  :root {
    --bg: #3a3a3c;
    --card: #ffffff;
    --navy: #1d3f8f;
    --orange: #f08a1c;
    --grey: #555a60;
    --ink: #2c2c2e;
  }
  * { margin: 0; padding: 0; box-sizing: border-box; }
  html, body {
    width: 1200px; height: 900px; overflow: hidden;
    background: var(--bg);
    font-family: "Jost", "Futura", sans-serif;
  }
  .stage {
    width: 1200px; height: 900px;
    display: flex; align-items: center; justify-content: center;
  }
  .card {
    width: 1050px; height: 600px;
    background: var(--card);
    border-radius: 46px;
    display: flex; flex-direction: column; align-items: center;
    padding-top: 44px;
    text-align: center;
  }
  .brand {
    display: flex; align-items: center; gap: 14px;
  }
  .brand-square {
    width: 30px; height: 30px; background: var(--navy);
  }
  .brand-name {
    font-size: 50px; font-weight: 600; color: var(--navy);
    letter-spacing: 1px;
  }
  .brand-title {
    margin-top: 6px;
    font-size: 22px; font-weight: 500; color: var(--navy);
    letter-spacing: 3px; text-transform: uppercase;
  }
  .brand-tagline {
    display: flex; align-items: center; gap: 10px;
    margin-top: 2px;
    font-size: 17px; color: var(--orange);
  }
  .brand-tagline .rule {
    width: 150px; height: 1.5px; background: var(--orange);
  }
  .services-heading {
    margin-top: 16px;
    font-size: 32px; font-weight: 600; color: var(--navy);
  }
  .services {
    list-style: none; margin-top: 8px;
    font-size: 26px; color: var(--grey); line-height: 1.36;
  }
  .services .dot { color: var(--orange); margin: 0 8px; }
  .promo {
    margin-top: 12px;
    font-size: 36px; font-weight: 600; color: var(--orange);
  }
  .phone {
    display: flex; align-items: center; gap: 14px;
    margin-top: 4px;
    font-size: 46px; font-weight: 400; color: var(--navy);
  }
  .phone svg { width: 40px; height: 40px; }
  .website {
    margin-top: 8px;
    font-size: 22px; font-weight: 500; color: var(--ink);
    letter-spacing: 9px;
  }
</style>
</head>
<body>
<main class="stage">
  <section class="card">
    <header class="brand-block">
      <div class="brand">
        <span class="brand-square"></span>
        <span class="brand-name">Bright Harbor Build</span>
      </div>
      <p class="brand-title">General Contractor for Realtors</p>
      <p class="brand-tagline"><span class="rule"></span>Remodels – Renovations – Repairs<span class="rule"></span></p>
    </header>

    <h2 class="services-heading">Our Services</h2>
    <ul class="services">
      <li><span class="dot">•</span>Water &amp; Mold Damage Experts<span class="dot">•</span>Painting: Interior/ Exterior</li>
      <li><span class="dot">•</span>Flooring: Wood / LVT / Carpet<span class="dot">•</span>Plumbing: Repairs &amp; Upgrades</li>
      <li><span class="dot">•</span>Electric: Lights &amp; Energy Efficient Upgrades<span class="dot">•</span>Kitchen &amp; Bath Remodels</li>
    </ul>

    <p class="promo">Fast Inspections Repair Billed Thru Escrow</p>

    <p class="phone">
      <svg viewBox="0 0 24 24" aria-hidden="true">
        <path fill="#1d3f8f" d="M6.6 10.8c1.4 2.8 3.8 5.1 6.6 6.6l2.2-2.2c.3-.3.7-.4 1-.2 1.1.4 2.3.6 3.6.6.6 0 1 .4 1 1V20c0 .6-.4 1-1 1C10.6 21 3 13.4 3 4c0-.6.4-1 1-1h3.5c.6 0 1 .4 1 1 0 1.3.2 2.5.6 3.6.1.3 0 .7-.2 1L6.6 10.8z"/>
        <path fill="none" stroke="#1d3f8f" stroke-width="1.6" stroke-linecap="round" d="M14 3.5a7 7 0 0 1 6.5 6.5M14 7a3.5 3.5 0 0 1 3 3"/>
      </svg>
      555-014-7390
    </p>
    <p class="website">BrightHarborBuild.example</p>
  </section>
</main>
</body>
</html>
```